Package Design for 15 lines of Tea

I need design variations for 15 different Tea lines.
The tea will be packaged in Tin cylinders.
I have attached several pictures to show you an example of the display we are modelling after along with other references.
The 15 tea lines are:
Study Tea
Ingredients: Brazilian Mate, Mint
Energy Boost Tea
Ingredients: Yunnan Coffee, Dark Puer
Relaxation Tea
Ingredients: Lotus Flower, South African Rooibos
Beauty Tea
Ingredients: Rose, Chrysanthemum, Red Dates, Huangqi
Sore Throat Tea
Ingredients: Honeysuckle, Pang Da Hai, Chamomile, Licorice Root
Get Well Tea
Ingredients: Ginger, Rooibos, Orange peel, Chinese Angelica
Diet Tea
Ingredients: Puer, Hibiscus, Lemongrass, Lotus Plumule
Bedtime Tea
Ingredients: Apple, Orange, Chamomile
South African Rooibos Tea
(pure)
Brazilian Yerba Mate Tea
(pure)
Long Jing Green Tea
(pure)
Darjeeling Black Tea
(pure)
Nepal Golden Tea
(Pure)
Bai Mu Dan White Tea
(pure)
Phoenix Oolong Tea
(pure)
Every Tea Blend should have three unique symbols that describe the purpose and theme of the blend. (!!Please don't make specific reference to the ingredients of the blends because some of these ingredients may be changed later. Stick to focusing on the intended purpose of the tea blend!!)
I would like the symbols to keep the same brushlike style that is consistent with our company logo.
Please keep the three block structure. I suggest keeping to just one color per tea blend. This will help each blend stand out between one another. I have a sample of the "Diet Tea" attached that I did myself to give you an idea of the structure I'm looking for, but obviously it's just my amateur version. Hope you can make them look far more appealing.
The ultimate goal is to build a picture language unique to our brand. As more products are released, we intend to potentially have hundreds of symbols, each with it's own meaning. So it would be nice when you present your pictures if you explain its intended meaning or message.
Deminsions:
Cylinder type 1: 82mm*38mmH
circular labels (along with your design) will be placed on the cap of product, and then the cylinder will be slanted on it's side to display the cap towards the customer.
Cylinder type 2: 65mm*152mmH
the labels will be placed on the side of the cylinder. In this version, try lining the three symbols in a vertical position. If this looks awful to you then feel free to go back to the horizontal style, but it would be nice to see what the vertical version looks like for reference.
Updates
Due to the scope of this project, please take note that I just increased my budget an additional 500 dollars more.
I also just added a 100 dollar second place prize. Don't want to see hard work unrewarded.
Feel free to send a few samples and I will provide prompt feedback. Please don't feel that you must submit all 15 lines at the same time.
Project Deadline Extended
Reason: I am extending the deadline as I feel there are more detailed revisions that need to be made until final selection.
Target Market(s)
Middle to Upper Class Consumers in China
Industry/Entity Type
It Company
Other font styles liked:
- font similar to font on company logo
Requirements
Must have
- Tea Designs must be in harmony with company logo and theme.
Should not have
- Avoid using Chinese characters as symbols. They may seem cool to westerners, but it's tacky for Chinese consumers.

```html
<!DOCTYPE html>
<html lang="en">
<head>
<meta charset="utf-8">
<title>Linden's Tea – Cap Labels</title>
<link href="https://fonts.googleapis.com/css2?family=Special+Elite&family=Roboto+Condensed:wght@400;700&display=swap" rel="stylesheet">
<style>
  :root {
    --bg: #ffffff;
    --ink: #1d1d1b;
    --band: #0d1113;
    --rule: rgba(255,255,255,0.85);
    --lime: #b3cb1c;
    --sage: #a4cf8e;
    --aqua: #a3dbd5;
    --sky: #86cdef;
    --icon-blue: #5ec6ee;
    --icon-orange: #f4a21f;
    --icon-yellow: #d9d923;
  }
  html, body {
    margin: 0;
    width: 1200px;
    height: 1000px;
    overflow: hidden;
    background: var(--bg);
  }
  .sheet {
    position: relative;
    width: 1200px;
    height: 1000px;
  }
  .label {
    position: absolute;
    top: 524px;
    width: 212px;
    height: 212px;
    border-radius: 50%;
    overflow: hidden;
    text-align: center;
    color: var(--ink);
  }
  .label::before {
    content: "";
    position: absolute;
    inset: 7px;
    border: 1px solid var(--rule);
    border-radius: 50%;
    pointer-events: none;
  }
  .label--sore-throat { left: 107px; background: var(--lime); }
  .label--relaxation  { left: 367px; background: var(--sage); }
  .label--long-jing   { left: 626px; background: var(--aqua); }
  .label--study       { left: 884px; background: var(--sky); }

  .brand {
    position: absolute;
    top: 20px;
    left: 0; right: 0;
    display: flex;
    justify-content: center;
    align-items: center;
    gap: 4px;
    font-family: "Roboto Condensed", sans-serif;
    font-weight: 700;
    font-size: 9px;
    line-height: 10px;
    color: var(--ink);
  }
  .brand__mark {
    width: 7px;
    height: 7px;
    background: var(--band);
  }
  .title {
    position: absolute;
    top: 56px;
    left: 0; right: 0;
    font-family: "Special Elite", monospace;
    font-size: 18px;
    line-height: 21px;
    white-space: nowrap;
  }
  .band {
    position: absolute;
    top: 102px;
    left: 0; right: 0;
    height: 42px;
    background: var(--band);
    display: flex;
    justify-content: center;
    align-items: center;
    gap: 14px;
  }
  .band svg {
    width: 24px;
    height: 24px;
    fill: none;
    stroke-width: 2.2;
    stroke-linecap: round;
    stroke-linejoin: round;
  }
  .i-blue   { stroke: var(--icon-blue); }
  .i-orange { stroke: var(--icon-orange); }
  .i-yellow { stroke: var(--icon-yellow); }
  .ingredients {
    position: absolute;
    top: 149px;
    left: 36px; right: 36px;
    font-family: "Special Elite", monospace;
    font-size: 5.5px;
    line-height: 7px;
    text-transform: uppercase;
    letter-spacing: 0.2px;
  }
</style>
</head>
<body>
<main class="sheet">

  <section class="label label--sore-throat">
    <div class="brand"><span class="brand__mark"></span>Linden's Tea</div>
    <div class="title">Sore Throat<br>Tea</div>
    <div class="band">
      <svg class="i-blue" viewBox="0 0 24 24" aria-label="bandage"><rect x="2" y="8" width="20" height="8" rx="4" transform="rotate(-45 12 12)"/><path d="M10 10l4 4M14 10l-4 4"/></svg>
      <svg class="i-orange" viewBox="0 0 24 24" aria-label="throat"><path d="M8 21v-5c-3-2-4-5-3-8 1-4 6-6 10-4 3 2 4 5 3 8l2 2-2 1v2h-3v4"/></svg>
      <svg class="i-yellow" viewBox="0 0 24 24" aria-label="feather"><path d="M4 20L18 6M18 6c2 4-1 10-8 10M18 6c-4-1-9 2-10 8"/></svg>
    </div>
    <div class="ingredients">Honeysuckle, Pang Da Hai,<br>Chamomile, Licorice Root</div>
  </section>

  <section class="label label--relaxation">
    <div class="brand"><span class="brand__mark"></span>Linden's Tea</div>
    <div class="title">Relaxation<br>Tea</div>
    <div class="band">
      <svg class="i-blue" viewBox="0 0 24 24" aria-label="cloud"><path d="M6 18h12a4 4 0 0 0 0-8 6 6 0 0 0-11-1 4.5 4.5 0 0 0-1 9z"/></svg>
      <svg class="i-orange" viewBox="0 0 24 24" aria-label="calm"><circle cx="12" cy="8" r="3"/><path d="M4 19h16M7 19c0-4 2-7 5-7s5 3 5 7"/></svg>
      <svg class="i-yellow" viewBox="0 0 24 24" aria-label="lotus"><path d="M12 19c-3-3-3-8 0-12 3 4 3 9 0 12zM12 19c-4 0-8-3-9-7 4 0 7 3 9 7zM12 19c4 0 8-3 9-7-4 0-7 3-9 7z"/></svg>
    </div>
    <div class="ingredients">Lotus Flower,<br>South African Rooibos</div>
  </section>

  <section class="label label--long-jing">
    <div class="brand"><span class="brand__mark"></span>Linden's Tea</div>
    <div class="title">Long Jing<br>Green Tea</div>
    <div class="band">
      <svg class="i-blue" viewBox="0 0 24 24" aria-label="tea cup"><path d="M4 9h13v4a6 6 0 0 1-6 6h-1a6 6 0 0 1-6-6zM17 10h1.5a2.5 2.5 0 0 1 0 5H16M3 21h16"/></svg>
      <svg class="i-orange" viewBox="0 0 24 24" aria-label="mountain"><path d="M2 20l7-12 4 6 3-4 6 10z"/></svg>
      <svg class="i-yellow" viewBox="0 0 24 24" aria-label="sun"><circle cx="12" cy="12" r="4"/><path d="M12 2v3M12 19v3M2 12h3M19 12h3M5 5l2 2M17 17l2 2M5 19l2-2M17 7l2-2"/></svg>
    </div>
  </section>

  <section class="label label--study">
    <div class="brand"><span class="brand__mark"></span>Linden's Tea</div>
    <div class="title">Study<br>Tea</div>
    <div class="band">
      <svg class="i-blue" viewBox="0 0 24 24" aria-label="light bulb"><path d="M9 16c0-3-3-4-3-8a6 6 0 0 1 12 0c0 4-3 5-3 8zM9 19h6M10 22h4"/></svg>
      <svg class="i-orange" viewBox="0 0 24 24" aria-label="book"><path d="M12 6c-3-2-6-2-9-1v14c3-1 6-1 9 1 3-2 6-2 9-1V5c-3-1-6-1-9 1zM12 6v14"/></svg>
      <svg class="i-yellow" viewBox="0 0 24 24" aria-label="magnifier"><circle cx="10" cy="10" r="6"/><path d="M14.5 14.5L21 21"/></svg>
    </div>
    <div class="ingredients">Brazilian Mate, Mint</div>
  </section>

</main>
</body>
</html>
```